New Business Card Design Project

Target Market(s)

Passing cards out

Industry/Entity Type

Asphalt contractor

Contact Information for Business Card

Ridgefold Paving

Colors
FFC000
F8CF3A
FAE287
FDF2CF
FEFAEE
F0912C
F2A743
F7CA91
FBE8D2
FDF5EE
EE7325
F08F49
F5BC92
FAE3D3
FDF4ED

Requirements
Must have
• Asphalt
Nice to have
• Would like to have 2 pictures on it of equipment

```html
<!DOCTYPE html>
<html lang="en">
<head>
<meta charset="utf-8">
<title>Ridgefold Paving – Business Card</title>
<link rel="stylesheet" href="https://fonts.googleapis.com/css2?family=Figtree:wght@400;500;700&display=swap">
<style>
  :root {
    --bg: #e6e6e6;
    --card: #ffffff;
    --orange-light: #f39423;
    --orange-dark: #d9682f;
    --ink: #1b1b1b;
    --ink-soft: #2a2a2a;
    --accent: #f0912c;
  }
  * { margin: 0; padding: 0; box-sizing: border-box; }
  html, body {
    width: 1200px; height: 1200px; overflow: hidden;
    background: var(--bg);
    font-family: "Figtree", sans-serif;
    color: var(--ink);
  }
  .card {
    position: absolute;
    left: 139px;
    width: 922px; height: 526px;
    background: var(--card);
    overflow: hidden;
  }
  .card--front { top: 58px; }
  .card--back { top: 618px; }

  .front-panel { position: absolute; inset: 0; width: 100%; height: 100%; }

  .contact-block { position: absolute; left: 80px; top: 94px; color: var(--ink); }
  .person-name { font-size: 36px; font-weight: 700; letter-spacing: 0.3px; line-height: 1.1; }
  .person-role { font-size: 23px; font-weight: 400; margin-top: 8px; color: var(--ink-soft); }

  .contact-list { list-style: none; margin-top: 50px; }
  .contact-item {
    display: flex; align-items: flex-start; gap: 14px;
    font-size: 24px; line-height: 36px; color: var(--ink-soft);
  }
  .contact-item--address { margin-top: 28px; }
  .contact-icon { width: 18px; height: 18px; flex: none; margin-top: 9px; fill: var(--ink); }

  .brand {
    position: absolute;
    display: flex; flex-direction: column; align-items: center; gap: 14px;
    transform: translate(-50%, -50%);
  }
  .card--front .brand { left: 699px; top: 267px; }
  .card--back .brand { left: 461px; top: 263px; }
  .brand-dot { width: 34px; height: 34px; border-radius: 50%; background: var(--accent); }
  .brand-name {
    font-size: 36px; font-weight: 700; color: var(--ink);
    text-align: center; line-height: 1.15; letter-spacing: 1px;
  }
</style>
</head>
<body>

<section class="card card--front" aria-label="Card front">
  <svg class="front-panel" viewBox="0 0 738 421" preserveAspectRatio="none" aria-hidden="true">
    <defs>
      <linearGradient id="panelGradient" x1="0" y1="0" x2="1" y2="1">
        <stop offset="0" stop-color="#f39423"/>
        <stop offset="1" stop-color="#d9682f"/>
      </linearGradient>
    </defs>
    <polygon fill="url(#panelGradient)" points="0,0 355,0 355,184 386,219 386,421 0,421"/>
    <polygon fill="url(#panelGradient)" points="375,0 400,0 400,421 397,421 397,219 375,194"/>
  </svg>

  <div class="contact-block">
    <h1 class="person-name">YOUR NAME</h1>
    <p class="person-role">Designation</p>
    <ul class="contact-list">
      <li class="contact-item">
        <svg class="contact-icon" viewBox="0 0 24 24"><path d="M6.6 10.8a15.1 15.1 0 0 0 6.6 6.6l2.2-2.2a1 1 0 0 1 1-.25 11.4 11.4 0 0 0 3.6.57 1 1 0 0 1 1 1V20a1 1 0 0 1-1 1A17 17 0 0 1 3 4a1 1 0 0 1 1-1h3.5a1 1 0 0 1 1 1c0 1.25.2 2.45.57 3.57a1 1 0 0 1-.25 1z"/></svg>
        <span>(610) 000-0000</span>
      </li>
      <li class="contact-item">
        <svg class="contact-icon" viewBox="0 0 24 24"><path d="M7 1h10a2 2 0 0 1 2 2v18a2 2 0 0 1-2 2H7a2 2 0 0 1-2-2V3a2 2 0 0 1 2-2zm0 3v14h10V4zm5 15.5a1 1 0 1 0 0 2 1 1 0 0 0 0-2z"/></svg>
        <span>(610) 000-0000</span>
      </li>
      <li class="contact-item">
        <svg class="contact-icon" viewBox="0 0 24 24"><path d="M2 5h20v14H2zm2 2v.5l8 5 8-5V7l-8 5z"/></svg>
        <span>www.ridgefold.com</span>
      </li>
      <li class="contact-item contact-item--address">
        <svg class="contact-icon" viewBox="0 0 24 24"><path d="M12 2a7 7 0 0 0-7 7c0 5.2 7 13 7 13s7-7.8 7-13a7 7 0 0 0-7-7zm0 9.5A2.5 2.5 0 1 1 12 6.5a2.5 2.5 0 0 1 0 5z"/></svg>
        <span>0/2 Kessler Ave Suite 0000,<br>Alder, PA 11111</span>
      </li>
    </ul>
  </div>

  <div class="brand">
    <span class="brand-dot" aria-hidden="true"></span>
    <p class="brand-name">RIDGEFOLD<br>PAVING</p>
  </div>
</section>

<section class="card card--back" aria-label="Card back">
  <div class="brand">
    <span class="brand-dot" aria-hidden="true"></span>
    <p class="brand-name">RIDGEFOLD<br>PAVING</p>
  </div>
</section>

</body>
</html>
```